Need a Creative 1 Page Website Design

Looking for a personal website. This is the current site and it needs to be updated. https://corvinlestfolio.com/
Reference - glassharbor.video
meridelstudios.nyc
Use the same font used in the current site. But we need to have a more creative website
follow this order and video list https://files.pelnorashare.com/doc/7Qx2LmVtRk9aWpZc3NyHbJd4FsUe6GoYi0TnXa8Kq/edit?usp=sharing
screenshots https://files.pelnorashare.com/folders/8Rk2NxWq5TzLpVe3HbYcJ7MdUa0Gs?usp=sharing
Make a creative personal website with mostly video content.
Target Market(s)
Music
Number of Pages Required
1 page
Look and feel

```html
<!DOCTYPE html>
<html lang="en">
<head>
<meta charset="utf-8">
<title>Corvin Lest — Portfolio</title>
<link href="https://fonts.googleapis.com/css2?family=Marcellus&family=Lato:wght@400&display=swap" rel="stylesheet">
<style>
:root{
  --page:#ffffff;
  --wine:#6a2034;
  --wine-deep:#4f1526;
  --crimson:#e3203d;
  --scarlet:#f13a3a;
  --ink:#ffffff;
  --rule:rgba(255,255,255,.28);
  --play-fill:#ffffff;
  --play-mark:#1d1420;
}
*{margin:0;padding:0;box-sizing:border-box}
html,body{width:839px;height:1200px;overflow:hidden;background:var(--page)}
body{position:relative;font-family:"Marcellus",serif;color:var(--ink)}

.site{position:absolute;overflow:hidden;
  background:
    radial-gradient(ellipse 40% 18% at 8% 40%,rgba(241,58,58,.75),transparent 70%),
    radial-gradient(ellipse 35% 14% at 95% 50%,rgba(227,32,61,.85),transparent 70%),
    radial-gradient(ellipse 45% 16% at 10% 92%,rgba(241,58,58,.8),transparent 70%),
    radial-gradient(ellipse 40% 14% at 90% 12%,rgba(227,32,61,.7),transparent 70%),
    radial-gradient(ellipse 30% 12% at 92% 88%,rgba(227,32,61,.8),transparent 70%),
    radial-gradient(ellipse 35% 12% at 6% 70%,rgba(241,58,58,.6),transparent 70%),
    linear-gradient(160deg,var(--wine) 0%,#7a2238 40%,var(--wine-deep) 100%);}
.site--desktop{left:22px;top:19px;width:576px;height:934px}
.site--mobile{left:618px;top:19px;width:199px;height:1153px}

.rule{position:absolute;height:1px;background:var(--rule)}
.brand{position:absolute;letter-spacing:.06em;line-height:1;white-space:nowrap}
.nav{position:absolute;display:flex;letter-spacing:.04em;line-height:1;white-space:nowrap}
.section-title{position:absolute;letter-spacing:.05em;line-height:1;font-weight:400;white-space:nowrap}

.gallery{position:absolute;display:grid}
.tile{position:relative}
.tile::before{content:"";position:absolute;left:50%;top:50%;border-radius:50%;background:var(--play-fill);transform:translate(-50%,-50%)}
.tile::after{content:"";position:absolute;left:50%;top:50%;border-style:solid;border-color:transparent transparent transparent var(--play-mark)}
.tile--big{grid-row:span 2}

.site--desktop .tile::before{width:15px;height:15px}
.site--desktop .tile::after{border-width:4px 0 4px 6px;transform:translate(-35%,-50%)}
.site--mobile .tile::before{width:12px;height:12px}
.site--mobile .tile::after{border-width:3.2px 0 3.2px 5px;transform:translate(-35%,-50%)}

.tone-crowd{background:linear-gradient(180deg,#4a5878 0%,#2b2f44 55%,#3a2a33 100%)}
.tone-park{background:linear-gradient(160deg,#6f7d4c 0%,#3c5138 60%,#5a4a3a 100%)}
.tone-night{background:linear-gradient(150deg,#1c2430 0%,#3a3c2c 45%,#121820 100%)}
.tone-doorway{background:linear-gradient(135deg,#6d6457 0%,#3d3c3e 55%,#8f8472 100%)}
.tone-phone{background:linear-gradient(135deg,#c9cbe0 0%,#8c89a8 55%,#3c3a4d 100%)}
.tone-street{background:linear-gradient(120deg,#9a9b9e 0%,#4f4e55 60%,#2c2b30 100%)}
.tone-skyline{background:linear-gradient(180deg,#a6a9a0 0%,#8c7764 60%,#6b4e3a 100%)}
.tone-car{background:linear-gradient(150deg,#1b1c22 0%,#2e3038 60%,#0f1014 100%)}
.tone-mono{background:linear-gradient(150deg,#111 0%,#555 50%,#1a1a1a 100%)}
.tone-dusk{background:linear-gradient(160deg,#3a3820 0%,#14170f 50%,#4a3d26 100%)}
.tone-beach{background:linear-gradient(180deg,#a9b8c2 0%,#c4b79a 35%,#7a6a4a 60%,#3a3440 100%)}
.tone-green{background:linear-gradient(150deg,#17321c 0%,#2a1614 55%,#0c1a10 100%)}
.tone-porch{background:linear-gradient(150deg,#6c6a62 0%,#3a3a3c 50%,#a8a6a0 100%)}
.tone-studio{background:linear-gradient(150deg,#c9c9c9 0%,#8a8a8a 40%,#2a2a2a 100%)}
.tone-yard{background:linear-gradient(150deg,#6e7e4e 0%,#8c8a84 45%,#3a3330 100%)}

.contact-title,.contact-email{position:absolute;left:0;right:0;text-align:center;line-height:1;letter-spacing:.04em;font-weight:400;white-space:nowrap}
.social{position:absolute;left:0;right:0;display:flex;justify-content:center;line-height:1;white-space:nowrap}
.copyright{position:absolute;left:0;right:0;text-align:center;font-family:"Lato",sans-serif;line-height:1;white-space:nowrap}

.menu-icon{position:absolute}
.menu-icon span{display:block;height:2px;background:var(--ink);margin-bottom:2.5px;border-radius:1px}
</style>
</head>
<body>

<main class="site site--desktop">
  <header>
    <div class="brand" style="left:36px;top:14px;font-size:21px">Corvin Lest</div>
    <nav class="nav" style="right:35px;top:21px;font-size:8px;gap:18px">
      <span>Direction</span><span>Executive Production</span><span>Commissioned</span><span>Contact</span>
    </nav>
    <div class="rule" style="left:36px;right:35px;top:50px"></div>
  </header>

  <section>
    <h2 class="section-title" style="left:36px;top:72px;font-size:13px">Executive Producer</h2>
    <div class="gallery" style="left:36px;top:100px;grid-template-columns:234px 129px 129px;grid-template-rows:86px 86px;gap:6px">
      <div class="tile tile--big tone-crowd" role="img" aria-label="Video still: group gathered around a motorbike on a street"></div>
      <div class="tile tone-park" role="img" aria-label="Video still: young man in a letterman jacket outdoors"></div>
      <div class="tile tone-night" role="img" aria-label="Video still: figure lit by a screen at night"></div>
      <div class="tile tone-doorway" role="img" aria-label="Video still: men standing in a doorway"></div>
      <div class="tile tone-phone" role="img" aria-label="Video still: hand holding a phone"></div>
    </div>
    <div class="rule" style="left:36px;right:35px;top:298px"></div>
  </section>

  <section>
    <h2 class="section-title" style="left:36px;top:314px;font-size:13px">Director</h2>
    <div class="gallery" style="left:36px;top:340px;grid-template-columns:129px 129px 234px;grid-template-rows:86px 86px;gap:6px">
      <div class="tile tone-street" role="img" aria-label="Video still: couple on a city street"></div>
      <div class="tile tone-skyline" role="img" aria-label="Video still: man on a rooftop with a city skyline"></div>
      <div class="tile tone-dusk" role="img" aria-label="Video still: man standing on a beach at night" style="grid-column:3;grid-row:1 / span 2"></div>
      <div class="tile tone-car" role="img" aria-label="Video still: man sitting in a car door"></div>
      <div class="tile tone-mono" role="img" aria-label="Video still: black and white close-up"></div>
    </div>
    <div class="rule" style="left:36px;right:35px;top:542px"></div>
  </section>

  <section>
    <h2 class="section-title" style="left:36px;top:558px;font-size:13px">Commissioner</h2>
    <div class="gallery" style="left:36px;top:586px;grid-template-columns:234px 129px 129px;grid-template-rows:86px 86px;gap:6px">
      <div class="tile tile--big tone-beach" role="img" aria-label="Video still: two men greeting on a beach"></div>
      <div class="tile tone-green" role="img" aria-label="Video still: figure in green light"></div>
      <div class="tile tone-porch" role="img" aria-label="Video still: man in a red beanie under a porch"></div>
      <div class="tile tone-studio" role="img" aria-label="Video still: man with a chain in a studio"></div>
      <div class="tile tone-yard" role="img" aria-label="Video still: man in a cap outdoors"></div>
    </div>
  </section>

  <footer>
    <h2 class="contact-title" style="top:786px;font-size:25px">Contact Us</h2>
    <p class="contact-email" style="top:822px;font-size:14px">corvinlestmgmt@pelnoramail.com</p>
    <div class="social" style="top:855px;font-size:7px;gap:12px">
      <span>Kestrel</span><span>Lumo</span><span>Framewell</span><span>Worknet</span><span>Reelhub</span>
    </div>
    <nav class="nav" style="left:0;right:0;justify-content:center;top:889px;font-size:8px;gap:18px">
      <span>Direction</span><span>Executive Production</span><span>Commissioned</span><span>Contact</span>
    </nav>
    <p class="copyright" style="top:908px;font-size:6px">Copyright © 2020 CompanyName All rights reserved.</p>
  </footer>
</main>

<main class="site site--mobile">
  <header>
    <div class="brand" style="left:9px;top:15px;font-size:16px">Corvin Lest</div>
    <div class="menu-icon" style="right:8px;top:17px;width:13px" aria-label="Menu"><span></span><span></span><span></span></div>
    <div class="rule" style="left:8px;right:8px;top:42px"></div>
  </header>

  <section>
    <h2 class="section-title" style="left:0;right:0;text-align:center;top:54px;font-size:12px">Executive Producer</h2>
    <div class="gallery" style="left:8px;top:75px;grid-template-columns:87px 87px;grid-template-rows:139px 58px 58px;column-gap:9px;row-gap:7px">
      <div class="tile tone-crowd" style="grid-column:1 / span 2" role="img" aria-label="Video still: group gathered around a motorbike on a street"></div>
      <div class="tile tone-park" role="img" aria-label="Video still: young man in a letterman jacket outdoors"></div>
      <div class="tile tone-night" role="img" aria-label="Video still: figure lit by a screen at night"></div>
      <div class="tile tone-doorway" role="img" aria-label="Video still: men standing in a doorway"></div>
      <div class="tile tone-phone" role="img" aria-label="Video still: hand holding a phone"></div>
    </div>
    <div class="rule" style="left:8px;right:8px;top:365px"></div>
  </section>

  <section>
    <h2 class="section-title" style="left:0;right:0;text-align:center;top:380px;font-size:12px">Director</h2>
    <div class="gallery" style="left:8px;top:404px;grid-template-columns:87px 87px;grid-template-rows:58px 58px 139px;column-gap:9px;row-gap:8px">
      <div class="tile tone-street" role="img" aria-label="Video still: couple on a city street"></div>
      <div class="tile tone-skyline" role="img" aria-label="Video still: man on a rooftop with a city skyline"></div>
      <div class="tile tone-car" role="img" aria-label="Video still: man sitting in a car door"></div>
      <div class="tile tone-mono" role="img" aria-label="Video still: black and white close-up"></div>
      <div class="tile tone-dusk" style="grid-column:1 / span 2" role="img" aria-label="Video still: man standing on a beach at night"></div>
    </div>
    <div class="rule" style="left:8px;right:8px;top:697px"></div>
  </section>

  <section>
    <h2 class="section-title" style="left:0;right:0;text-align:center;top:712px;font-size:12px">Commissioner</h2>
    <div class="gallery" style="left:8px;top:734px;grid-template-columns:87px 87px;grid-template-rows:139px 58px 58px;column-gap:9px;row-gap:7px">
      <div class="tile tone-beach" style="grid-column:1 / span 2" role="img" aria-label="Video still: two men greeting on a beach"></div>
      <div class="tile tone-green" role="img" aria-label="Video still: figure in green light"></div>
      <div class="tile tone-porch" role="img" aria-label="Video still: man in a red beanie under a porch"></div>
      <div class="tile tone-studio" role="img" aria-label="Video still: man with a chain in a studio"></div>
      <div class="tile tone-yard" role="img" aria-label="Video still: man in a cap outdoors"></div>
    </div>
  </section>

  <footer>
    <h2 class="contact-title" style="top:1021px;font-size:15px">Contact Us</h2>
    <p class="contact-email" style="top:1045px;font-size:9px;letter-spacing:.02em">corvinlestmgmt@pelnoramail.com</p>
    <div class="social" style="top:1067px;font-size:6px;gap:7px">
      <span>Kestrel</span><span>Lumo</span><span>Framewell</span><span>Worknet</span><span>Reelhub</span>
    </div>
    <nav class="nav" style="left:0;right:0;justify-content:center;top:1095px;font-size:7.5px;gap:18px">
      <span>Direction</span><span>Executive Production</span>
    </nav>
    <nav class="nav" style="left:0;right:0;justify-content:center;top:1109px;font-size:7.5px;gap:18px">
      <span>Commissioned</span><span>Contact</span>
    </nav>
    <p class="copyright" style="top:1129px;font-size:5.5px">Copyright © 2020 CompanyName All rights reserved.</p>
  </footer>
</main>

</body>
</html>
```